VERIDAX Need a luxury modern business card designed.

Need a luxury modern business card designed. refer to the uploaded files for the company name and logo in the zip file under source files. i will making my descion on monday. so please send in before then so if we need to edit we will have the time. we have a trade show coming up and im on a deadline for printer.

Target Market(s)

high end clients

Contact Information for Business Card

Company nAme and logo. Calvin Ostrow Co-Founder / Project Manager Office # 416-555-0193 Cell # 416-555-0147 VERIDAX.CA Calvin@veridax.ca

Font styles to use
Other font styles liked:
• Modern

Requirements
Must have
• Company name and logo, contact info, using the black, gold and white color scheme.

```html
<!DOCTYPE html>
<html lang="en">
<head>
<meta charset="utf-8">
<title>VERIDAX — Business Card</title>
<link href="https://fonts.googleapis.com/css2?family=Arimo:wght@400;700&display=swap" rel="stylesheet">
<style>
  :root {
    --stage: #0b0b0b;
    --card: #2a2a2b;
    --card-edge: #a8955f;
    --gold: #b9a46c;
    --white: #f2f2f0;
    --emboss: #3a3a3b;
    --emboss-light: #4a4a4b;
    --emboss-dark: #1c1c1d;
  }
  * { margin: 0; padding: 0; box-sizing: border-box; }
  html, body {
    width: 1200px; height: 822px; overflow: hidden;
    background: var(--stage);
    font-family: "Arimo", Arial, sans-serif;
  }
  .stage {
    width: 1200px; height: 822px;
    display: flex; align-items: center; justify-content: center; gap: 60px;
  }
  .card {
    width: 520px; height: 297px;
    background: var(--card);
    border: 1.5px solid var(--card-edge);
    border-radius: 3px;
    display: flex; flex-direction: column; align-items: center; justify-content: center;
    text-align: center;
  }
  .brand { display: flex; flex-direction: column; align-items: center; }
  .brand-name {
    display: flex; align-items: center; gap: 12px;
    font-weight: 400; font-size: 34px; letter-spacing: 9px;
    color: var(--white);
  }
  .brand-square { width: 10px; height: 10px; background: var(--gold); }
  .brand-tagline {
    margin-top: 6px; font-size: 9px; letter-spacing: 4px; color: var(--white);
  }
  .contact { margin-top: 26px; font-size: 14px; color: var(--white); line-height: 1.45; }
  .contact-name {
    color: var(--gold); font-weight: 700; font-size: 17px; letter-spacing: 0.5px;
    text-transform: uppercase;
  }
  .contact-divider { width: 150px; height: 1px; background: #4a4a4a; margin: 6px auto; }
  .label { color: var(--gold); font-weight: 700; }
  .card--back .brand-name {
    color: var(--emboss);
    font-size: 40px; letter-spacing: 11px;
    text-shadow: -1px -1px 0 var(--emboss-dark), 1px 1px 0 var(--emboss-light);
  }
  .card--back .brand-square {
    background: var(--emboss);
    box-shadow: -1px -1px 0 var(--emboss-dark), 1px 1px 0 var(--emboss-light);
  }
  .card--back .brand-tagline { color: var(--emboss-light); }
</style>
</head>
<body>
  <main class="stage">
    <section class="card card--front">
      <div class="brand">
        <div class="brand-name"><span class="brand-square"></span>VERIDAX</div>
        <div class="brand-tagline">LUXURY LANDSCAPES</div>
      </div>
      <div class="contact">
        <div class="contact-name">Calvin Ostrow</div>
        <div class="contact-title">Co-Founder / Project Manager</div>
        <div class="contact-divider"></div>
        <div class="contact-phones"><span class="label">P:</span> 416-555-0193 &nbsp;| <span class="label">M:</span> 416-555-0147</div>
        <div class="contact-web">veridax.ca calvin@veridax.ca</div>
      </div>
    </section>
    <section class="card card--back">
      <div class="brand">
        <div class="brand-name"><span class="brand-square"></span>VERIDAX</div>
        <div class="brand-tagline">LUXURY LANDSCAPES</div>
      </div>
    </section>
  </main>
</body>
</html>
```